Use your magic to make a startup company look established*

We are in need of a website that gives the appearance that we are established rather than new. Our audience is comprised of senior executives in technology professional services companies, financial people (conservative) that invest in them, and executives in companies that are in need of their services. The site therefore needs to lean towards the conservative side while being modern and professional.

This should be a fairly simple site.

- About us
- Services
- Contacts
- Content (Articles)

It should be SEO friendly and easy to add content or sub pages. A responsive design is mandatory.

Target Market(s)

We work with executives and investors in professional services companies to more effectively compete in the already crowded “digital transformation” market.

Industry/Entity Type

Professional Service

Coding

Coded - Design and coding required

Number of Pages Required

5+ page

Font styles to use
Sans Serif

Requirements
Must have
• - Responsive design
- Easy to add/change content
- Easy to add additional pages

```html
<!DOCTYPE html>
<html lang="en">
<head>
<meta charset="utf-8">
<title>Summit Crest Partners</title>
<link href="https://fonts.googleapis.com/css2?family=Montserrat:wght@500;600;700&family=Roboto:wght@300;400;500;700&display=swap" rel="stylesheet">
<style>
:root{
  --gold:#b8913a;
  --gold-light:#d4ad52;
  --ink:#1c1c1c;
  --text:#555;
  --grey:#c4c4c4;
  --hero:#fdf4ec;
  --panel:#f4f4f4;
  --dark:#111;
  --card-dark:#232323;
}
*{box-sizing:border-box;margin:0;padding:0}
html,body{width:1200px;height:3759px;overflow:hidden}
body{position:relative;font-family:'Roboto',sans-serif;color:var(--text);background:#fff}
.abs{position:absolute}
a{color:inherit;text-decoration:none}

/* header */
.header{left:0;top:0;width:1200px;height:150px;background:#fff;border-bottom:1px solid #eee}
.logo{display:flex;align-items:center;gap:14px}
.logo-square{width:20px;height:20px;background:var(--gold);flex:none}
.logo-name{font-family:'Montserrat',sans-serif;font-weight:500;color:#777;letter-spacing:2px;line-height:1.15}
.nav{left:387px;top:66px;display:flex;gap:29px;font-size:16px;color:#222;font-weight:500}
.nav .active{color:var(--gold)}
.cta{left:927px;top:0;width:273px;height:150px;background:var(--gold);color:#fff;text-align:center;padding-top:52px}
.cta small{display:block;font-size:15px;font-weight:500}
.cta strong{display:flex;justify-content:center;align-items:center;gap:8px;font-size:24px;font-weight:700;margin-top:4px}

/* hero */
.hero{left:0;top:150px;width:1200px;height:568px;background:var(--hero)}
.hero-wave{top:0;height:568px}
.hero-frame{left:400px;top:213px;width:400px;height:397px}
.hero-title{left:400px;top:296px;width:400px;text-align:center;font-weight:700;font-size:40px;line-height:51px;color:var(--ink)}
.btn-gold{left:400px;top:563px;width:165px;height:46px;background:var(--gold);color:#fff;font-size:18px;display:flex;align-items:center;justify-content:center}

/* section titles */
.sec-title{font-family:'Montserrat',sans-serif;font-weight:700;font-size:35px;color:var(--ink);letter-spacing:1px;white-space:nowrap}
.sec-title span{color:var(--gold)}
.sec-title.on-dark{color:#fff}
.sec-title.on-dark span{color:#fff;font-weight:500}
.title-box{border:2px solid var(--gold)}

/* about */
.about-text{left:98px;top:874px;width:508px;font-size:11.5px;line-height:18.5px;color:#333}
.feature{display:flex;gap:14px;width:250px}
.feature .ic{width:52px;height:52px;border-radius:50%;background:var(--gold);flex:none;display:flex;align-items:center;justify-content:center}
.feature h4{font-size:16px;font-weight:700;color:var(--ink);margin:2px 0 5px}
.feature p{font-size:10.5px;line-height:16px;color:#444}
.about-art{left:720px;top:790px;width:340px;height:380px;border-radius:50% 50% 45% 45%;background:radial-gradient(circle at 50% 60%,#e9417a 0,#f5b93a 20%,#4a8be0 40%,#dce9fb 62%,#fff 72%)}

/* services */
.services{left:0;top:1204px;width:1200px;height:582px;background:var(--panel)}
.svc{width:232px;height:313px}
.svc .frame{position:absolute;inset:0;border:7px solid var(--grey)}
.svc .frame::before{content:"";position:absolute;left:30px;right:30px;top:-7px;height:7px;background:var(--panel)}
.svc .frame::after{content:"";position:absolute;top:130px;bottom:20px;left:-7px;width:7px;background:var(--panel)}
.svc .head{position:absolute;left:13px;top:13px;width:206px;height:128px;background:var(--card-dark);color:#fff;text-align:center;padding-top:25px;font-size:15.5px}
.svc .head svg{display:block;margin:0 auto 14px}
.svc p{position:absolute;left:28px;top:158px;width:176px;text-align:center;font-size:11.5px;line-height:17px;color:#888}
.svc .more{position:absolute;left:59px;top:259px;width:114px;height:31px;border:2px solid #ccc;border-radius:16px;font-size:11.5px;font-weight:500;color:#444;display:flex;align-items:center;justify-content:center;background:#fff}
.svc.featured .frame{border-color:var(--gold)}
.svc.featured .head{background:var(--gold)}
.svc.featured .more{background:var(--gold);border-color:var(--gold);color:#fff}

/* stats */
.stats{left:0;top:1786px;width:1200px;height:205px;background:linear-gradient(90deg,#2a2a2a,#5a5a5a 45%,#3b3b3b 70%,#1c1c1c)}
.stat{width:220px;text-align:center;color:#fff}
.stat b{display:block;font-family:'Montserrat',sans-serif;font-size:40px;font-weight:700;line-height:44px;margin-top:6px}
.stat small{font-size:13.5px}

/* clients */
.clients{left:0;top:1991px;width:1200px;height:514px;background:#f4f2f0}
.quote{width:313px;height:180px;background:#fff;padding:40px 22px 0;text-align:center;font-size:12.5px;line-height:18px;color:#777}
.quote::after{content:"";position:absolute;left:80px;bottom:-16px;border-right:18px solid transparent;border-top:16px solid #fff}
.person{display:flex;align-items:center;gap:14px}
.avatar{width:64px;height:64px;border-radius:50%;background:radial-gradient(circle,#8a8f99,#3d4450)}
.person b{display:block;color:var(--gold);font-size:14px;font-family:'Montserrat',sans-serif}
.person small{font-size:12.5px;color:#333;font-weight:500}

/* articles */
.article{width:317px;height:358px;background:#fff;box-shadow:0 0 6px rgba(0,0,0,.15);border:3px solid #fff}
.article .photo{height:167px}
.date{position:absolute;right:8px;top:8px;width:46px;height:46px;background:var(--gold);color:#fff;text-align:center;font-weight:700;font-size:18px;line-height:17px;padding-top:6px}
.date small{display:block;font-size:12px}
.article .meta{padding:14px 15px 0;font-size:14.5px;color:var(--gold)}
.article h3{padding:6px 15px 0;font-size:19.5px;font-weight:700;color:var(--ink)}
.article p{padding:5px 15px 0;font-size:15px;line-height:19px;color:#777}
.article .foot{position:absolute;left:20px;right:20px;bottom:18px;display:flex;justify-content:space-between;font-size:15px;font-weight:700;color:var(--gold)}

/* contact */
.contact{left:0;top:3125px;width:1200px;height:578px;background:radial-gradient(ellipse at 40% 45%,#1f1f1f,#0e0e0e 70%)}
.info{left:128px;color:#fff;font-size:15px;display:flex;gap:12px;align-items:flex-start;width:340px;line-height:18px}
.field{left:540px;width:532px;background:#fff;border:1px solid #ddd;font-size:12px;color:#666;padding:12px 10px}
.submit{left:540px;top:3617px;width:96px;height:32px;border:1px solid #fff;color:#fff;font-size:13px;display:flex;align-items:center;justify-content:center}
.footer{left:0;top:3703px;width:1200px;height:56px;background:var(--gold);border-top:4px solid #111;color:#fff;font-size:12.5px;text-align:center;line-height:52px}
</style>
</head>
<body>

<!-- header -->
<header class="abs header">
  <div class="abs logo" style="left:98px;top:44px">
    <div class="logo-square"></div>
    <div class="logo-name" style="font-size:19px">SUMMIT<br>CREST<br>PARTNERS</div>
  </div>
  <nav class="abs nav">
    <a class="active">HOME</a><a>ABOUT US</a><a>SERVICES</a><a>CONTENT</a><a>CONTACTS</a>
  </nav>
  <div class="abs cta">
    <small>100% FREE CONSULTATION</small>
    <strong><svg width="22" height="22" viewBox="0 0 24 24"><path fill="#fff" d="M6.6 10.8a15 15 0 0 0 6.6 6.6l2.2-2.2c.3-.3.7-.4 1-.2 1.1.4 2.3.6 3.6.6.6 0 1 .4 1 1V20c0 .6-.4 1-1 1A17 17 0 0 1 3 4c0-.6.4-1 1-1h3.5c.6 0 1 .4 1 1 0 1.3.2 2.5.6 3.6.1.3 0 .7-.2 1z"/></svg>(800) 555-0142</strong>
  </div>
</header>

<!-- hero -->
<section class="abs hero">
  <div class="abs hero-wave" role="img" aria-label="Flowing golden line-art waves" style="left:0;width:420px;background:radial-gradient(ellipse at 20% 70%,rgba(216,180,130,.35),transparent 65%)"></div>
  <div class="abs hero-wave" role="img" aria-label="Flowing golden line-art waves" style="left:760px;width:440px;background:radial-gradient(ellipse at 70% 25%,rgba(216,180,130,.35),transparent 65%)"></div>
</section>
<svg class="abs hero-frame" viewBox="0 0 400 397">
  <defs><linearGradient id="g" x1="0" y1="0" x2="1" y2="1"><stop offset="0" stop-color="#d9b548"/><stop offset="1" stop-color="#9a7530"/></linearGradient>
  <linearGradient id="s" x1="0" y1="0" x2="1" y2="0"><stop offset="0" stop-color="#555"/><stop offset="1" stop-color="#aaa"/></linearGradient></defs>
  <polyline points="6,350 6,6 270,6" fill="none" stroke="url(#g)" stroke-width="12"/>
  <polyline points="282,6 394,6 394,118" fill="none" stroke="url(#s)" stroke-width="12"/>
  <polyline points="394,130 394,391 180,391" fill="none" stroke="url(#g)" stroke-width="12"/>
</svg>
<h1 class="abs hero-title">TECHNOLOGY<br>PROFESSIONAL<br>SERVICES<br>COMPANIES</h1>
<a class="abs btn-gold">KNOW MORE</a>
<svg class="abs" style="left:588px;top:655px" width="24" height="40" viewBox="0 0 24 40"><rect x="4" y="2" width="16" height="26" rx="8" fill="none" stroke="#b8913a" stroke-width="1.5"/><line x1="12" y1="8" x2="12" y2="13" stroke="#b8913a" stroke-width="1.5"/><polyline points="7,32 12,37 17,32" fill="none" stroke="#b8913a" stroke-width="1.5"/></svg>

<!-- about -->
<div class="abs title-box" style="left:180px;top:768px;width:139px;height:80px"></div>
<h2 class="abs sec-title" style="left:98px;top:785px">ABOUT <span>US</span></h2>
<p class="abs about-text">Lorem Ipsum is simply dummy text of the printing and typesetting industry. Lorem Ipsum has been the industry's standard dummy text ever since the 1500s, when an unknown printer took a galley of type and scrambled it to make a type specimen book. It has survived not only five centuries, but also the leap into electronic typesetting.</p>
<div class="abs feature" style="left:98px;top:975px">
  <div class="ic"><svg width="28" height="24" viewBox="0 0 28 24"><circle cx="14" cy="7" r="5" fill="#fff"/><circle cx="5" cy="9" r="3.5" fill="#fff"/><circle cx="23" cy="9" r="3.5" fill="#fff"/><path d="M6 22a8 8 0 0 1 16 0z" fill="#fff"/></svg></div>
  <div><h4>Heading One</h4><p>Lorem Ipsum is simply dummy text of the printing and typesetting.</p></div>
</div>
<div class="abs feature" style="left:355px;top:975px">
  <div class="ic"><svg width="28" height="28" viewBox="0 0 28 28" fill="none" stroke="#fff" stroke-width="2"><circle cx="14" cy="14" r="11"/><circle cx="14" cy="14" r="6"/><line x1="14" y1="14" x2="25" y2="3"/></svg></div>
  <div><h4>Heading Three</h4><p>Lorem Ipsum is simply dummy text of the printing and typesetting.</p></div>
</div>
<div class="abs feature" style="left:98px;top:1072px">
  <div class="ic"><svg width="30" height="20" viewBox="0 0 30 20" fill="none" stroke="#fff" stroke-width="2"><path d="M1 10C6 2 24 2 29 10 24 18 6 18 1 10z"/><circle cx="15" cy="10" r="4" fill="#fff"/></svg></div>
  <div><h4>Heading Two</h4><p>Lorem Ipsum is simply dummy text of the printing and typesetting.</p></div>
</div>
<div class="abs feature" style="left:355px;top:1072px">
  <div class="ic"><svg width="28" height="24" viewBox="0 0 28 24" fill="none" stroke="#fff" stroke-width="2"><rect x="1" y="3" width="24" height="18" rx="2"/><line x1="1" y1="9" x2="25" y2="9"/><rect x="18" y="14" width="9" height="8" fill="#fff"/></svg></div>
  <div><h4>Heading Four</h4><p>Lorem Ipsum is simply dummy text of the printing and typesetting.</p></div>
</div>
<div class="abs about-art" role="img" aria-label="Isometric illustration of two business people on a circular data dashboard with charts"></div>

<!-- services -->
<section class="abs services"></section>
<div class="abs title-box" style="left:600px;top:1268px;width:168px;height:78px"></div>
<h2 class="abs sec-title" style="left:462px;top:1285px">OUR <span>SERVICES</span></h2>

<div class="abs svc" style="left:98px;top:1393px"><div class="frame"></div>
  <div class="head"><svg width="48" height="44" viewBox="0 0 48 44" fill="none" stroke="#fff" stroke-width="1.6"><rect x="3" y="3" width="42" height="28"/><polyline points="10,24 18,14 26,20 38,9"/><line x1="24" y1="31" x2="14" y2="42"/><line x1="24" y1="31" x2="34" y2="42"/></svg>FINANCIAL CONSULTING</div>
  <p>Lorem Ipsum is simply dummy text of the printing and typesetting industry. Lorem Ipsum has been the industry's standard dummy text ever</p>
  <a class="more">READ MORE</a></div>
<div class="abs svc featured" style="left:355px;top:1393px"><div class="frame"></div>
  <div class="head"><svg width="48" height="48" viewBox="0 0 48 48" fill="none" stroke="#fff" stroke-width="1.6"><path d="M16 22a8 8 0 1 1 16 0c0 5-4 7-4 12h-8c0-5-4-7-4-12z"/><line x1="20" y1="38" x2="28" y2="38"/><line x1="21" y1="42" x2="27" y2="42"/><line x1="24" y1="2" x2="24" y2="7"/><line x1="8" y1="10" x2="12" y2="13"/><line x1="40" y1="10" x2="36" y2="13"/></svg>SUSTAINABILITY</div>
  <p>Lorem Ipsum is simply dummy text of the printing and typesetting industry. Lorem Ipsum has been the industry's standard dummy text ever</p>
  <a class="more">READ MORE</a></div>
<div class="abs svc" style="left:612px;top:1393px"><div class="frame"></div>
  <div class="head"><svg width="48" height="48" viewBox="0 0 48 48" fill="none" stroke="#fff" stroke-width="1.6"><circle cx="24" cy="24" r="20"/><polyline points="24,12 24,24 32,28"/></svg>RISK MANAGEMENT</div>
  <p>Lorem Ipsum is simply dummy text of the printing and typesetting industry. Lorem Ipsum has been the industry's standard dummy text ever</p>
  <a class="more">READ MORE</a></div>
<div class="abs svc" style="left:869px;top:1393px"><div class="frame"></div>
  <div class="head"><svg width="48" height="48" viewBox="0 0 48 48" fill="none" stroke="#fff" stroke-width="1.6"><circle cx="24" cy="18" r="10"/><path d="M12 18a12 12 0 0 1 24 0"/><rect x="9" y="16" width="4" height="8"/><rect x="35" y="16" width="4" height="8"/><path d="M8 44c2-9 8-12 16-12s14 3 16 12z"/></svg>SUPPPORT TEAM</div>
  <p>Lorem Ipsum is simply dummy text of the printing and typesetting industry. Lorem Ipsum has been the industry's standard dummy text ever</p>
  <a class="more">READ MORE</a></div>

<!-- stats -->
<section class="abs stats" role="img" aria-label="Dark city skyscrapers backdrop"></section>
<div class="abs stat" style="left:130px;top:1823px"><svg width="54" height="54" viewBox="0 0 54 54" fill="none" stroke="#fff" stroke-width="3"><path d="M48 22A22 22 0 1 1 38 8"/><polyline points="16,26 25,35 49,9"/></svg><b>15000+</b><small>SUCESSFULL PROJECTS</small></div>
<div class="abs stat" style="left:372px;top:1823px"><svg width="54" height="54" viewBox="0 0 54 54" fill="none" stroke="#fff" stroke-width="2.5"><circle cx="27" cy="29" r="21"/><path d="M9 22c6-12 30-14 36 0"/><path d="M19 36c4 5 12 5 16 0"/></svg><b>700+</b><small>HAPPY CUSTOMERS</small></div>
<div class="abs stat" style="left:623px;top:1823px"><svg width="84" height="54" viewBox="0 0 84 54" fill="none" stroke="#fff" stroke-width="2.5"><circle cx="42" cy="16" r="9"/><path d="M26 50c0-14 8-20 16-20s16 6 16 20z"/><circle cx="18" cy="20" r="7"/><path d="M4 50c0-11 6-15 14-15"/><circle cx="66" cy="20" r="7"/><path d="M80 50c0-11-6-15-14-15"/></svg><b>2450+</b><small>TEAM MEMBERS</small></div>
<div class="abs stat" style="left:858px;top:1823px"><svg width="54" height="54" viewBox="0 0 54 54" fill="none" stroke="#fff" stroke-width="2.5"><path d="M15 4h24v14a12 12 0 0 1-24 0z"/><path d="M15 9H6c0 8 4 12 10 13M39 9h9c0 8-4 12-10 13"/><line x1="27" y1="30" x2="27" y2="40"/><rect x="17" y="40" width="20" height="8"/></svg><b>468+</b><small>AWARDS WON</small></div>

<!-- clients -->
<section class="abs clients"></section>
<div class="abs title-box" style="left:600px;top:2041px;width:235px;height:78px"></div>
<h2 class="abs sec-title" style="left:416px;top:2060px">OUR HAPPY <span>CLIENTS</span></h2>
<div class="abs quote" style="left:100px;top:2161px">Esse maxime tempore maiores laboriosam nobis, aut cum quidem est ab ipsam soluta voluptate totam quibusdam quo neque Lorem ipsum dolor sit amet, consectetur adipiscing elit, sed do eiusmod</div>
<div class="abs quote" style="left:443px;top:2161px">Esse maxime tempore maiores laboriosam nobis, aut cum quidem est ab ipsam soluta voluptate totam quibusdam quo neque Lorem ipsum dolor sit amet, consectetur adipiscing elit, sed do eiusmod</div>
<div class="abs quote" style="left:786px;top:2161px">Esse maxime tempore maiores laboriosam nobis, aut cum quidem est ab ipsam soluta voluptate totam quibusdam quo neque Lorem ipsum dolor sit amet, consectetur adipiscing elit, sed do eiusmod</div>
<div class="abs person" style="left:98px;top:2356px"><div class="avatar" role="img" aria-label="Client portrait"></div><div><b>DANIEL HART</b><small>Project Manager</small></div></div>
<div class="abs person" style="left:441px;top:2356px"><div class="avatar" role="img" aria-label="Client portrait"></div><div><b>DANIEL HART</b><small>Project Manager</small></div></div>
<div class="abs person" style="left:784px;top:2356px"><div class="avatar" role="img" aria-label="Client portrait"></div><div><b>DANIEL HART</b><small>Project Manager</small></div></div>
<svg class="abs" style="left:569px;top:2453px" width="60" height="8"><rect width="17" height="6" rx="3" fill="#b8913a"/><rect x="21" width="17" height="6" rx="3" fill="#222"/><rect x="42" width="17" height="6" rx="3" fill="#222"/></svg>

<!-- articles -->
<div class="abs title-box" style="left:600px;top:2573px;width:210px;height:78px"></div>
<h2 class="abs sec-title" style="left:439px;top:2591px">RECENT <span>ARTICLES</span></h2>
<article class="abs article" style="left:98px;top:2690px">
  <div class="photo" role="img" aria-label="Two business people walking outdoors" style="background:linear-gradient(135deg,#b79a7a,#4a3f38 55%,#8e8a80)"></div>
  <div class="date">30<small>JUN</small></div>
  <div class="meta">by admin | Latest Blog</div><h3>LOREM IPSUM IS SIMPLY</h3><p>Lorem Ipsum is simply dummy text of the printing and typesetting industry.</p>
  <div class="foot"><span>READ MORE</span><span style="font-weight:500">&#9633; 0 comment</span></div>
</article>
<article class="abs article" style="left:441px;top:2690px">
  <div class="photo" role="img" aria-label="City skyline with gold overlay" style="background:linear-gradient(180deg,#c2a060,#9d7e45);position:relative"><svg style="position:absolute;left:139px;top:66px" width="34" height="34" viewBox="0 0 34 34"><circle cx="17" cy="17" r="16" fill="#fff"/><path d="M12 20l8-8M13 16l-2 2a3 3 0 0 0 4 4l2-2M21 18l2-2a3 3 0 0 0-4-4l-2 2" stroke="#b8913a" stroke-width="2" fill="none"/></svg></div>
  <div class="meta">by admin | Latest Blog</div><h3>LOREM IPSUM IS SIMPLY</h3><p>Lorem Ipsum is simply dummy text of the printing and typesetting industry.</p>
  <div class="foot"><span>READ MORE</span><span style="font-weight:500">&#9633; 0 comment</span></div>
</article>
<article class="abs article" style="left:784px;top:2690px">
  <div class="photo" role="img" aria-label="Smiling man working at an office desk" style="background:linear-gradient(135deg,#e6e6e6,#8d8d8d 50%,#3b3b3b)"></div>
  <div class="date">30<small>JUN</small></div>
  <div class="meta">by admin | Latest Blog</div><h3>LOREM IPSUM IS SIMPLY</h3><p>Lorem Ipsum is simply dummy text of the printing and typesetting industry.</p>
  <div class="foot"><span>READ MORE</span><span style="font-weight:500">&#9633; 0 comment</span></div>
</article>

<!-- contact -->
<section class="abs contact" role="img" aria-label="Faint world map on dark background"></section>
<div class="abs title-box" style="left:607px;top:3173px;width:164px;height:78px"></div>
<h2 class="abs sec-title on-dark" style="left:484px;top:3191px">CONTACT <span>US</span></h2>
<div class="abs logo" style="left:128px;top:3322px;gap:20px">
  <div class="logo-square" style="width:28px;height:28px"></div>
  <div class="logo-name" style="font-size:26px;color:#aaa;letter-spacing:3px;line-height:1.25">SUMMIT<br>CREST<br>PARTNERS</div>
</div>
<div class="abs info" style="top:3482px"><svg width="16" height="20" viewBox="0 0 16 20"><path d="M8 0a8 8 0 0 1 8 8c0 6-8 12-8 12S0 14 0 8a8 8 0 0 1 8-8z" fill="#fff"/><circle cx="8" cy="8" r="3" fill="#111"/></svg><span><b>Address:</b> Lorem Ipsum is simply dummy text of the printing and typesetting</span></div>
<div class="abs info" style="top:3542px"><svg width="20" height="14" viewBox="0 0 20 14" fill="none" stroke="#fff" stroke-width="1.4"><rect x="1" y="1" width="18" height="12"/><polyline points="1,1 10,8 19,1"/></svg><span><b>Mail Id:</b> hello@summitcrest.example</span></div>
<div class="abs info" style="top:3580px;width:380px"><svg width="14" height="18" viewBox="0 0 14 18" fill="none" stroke="#fff" stroke-width="1.4"><rect x="1" y="1" width="12" height="16" rx="2"/><line x1="5" y1="14" x2="9" y2="14"/></svg><span><b>Phone:</b> +1 555 0142 7788 / +1 555 0199 2041</span></div>
<div class="abs field" style="top:3300px;height:38px">Name</div>
<div class="abs field" style="top:3349px;height:38px">Email</div>
<div class="abs field" style="top:3399px;height:38px">Phone</div>
<div class="abs field" style="top:3450px;height:138px">Message</div>
<a class="abs submit">Submit</a>

<footer class="abs footer">©2021 Summit Crest Partners | All Rights Reserved</footer>
</body>
</html>
```